Modified Business card

We have developed a new logo for the business, and want thou to tray and incorporate it into the business card design that you have done for us.

I am going to upload the logo files. We like the simple clean look that you have on the card, so if you can keep the look incorporating the logo.

Industry/Entity Type

Business

```html
<!DOCTYPE html>
<html lang="en">
<head>
<meta charset="utf-8">
<title>Halvorsen Works – Business Card Variants</title>
<link href="https://fonts.googleapis.com/css2?family=Merriweather:wght@400;700&display=swap" rel="stylesheet">
<style>
  :root {
    --frame-red: #ee1c1c;
    --frame-dark: #8a0000;
    --mark-red: #d0202a;
    --brand-grey: #555558;
    --card-dark: #000000;
    --card-light: #ffffff;
    --text-on-dark: #ffffff;
    --text-on-light: #000000;
  }
  html, body {
    margin: 0;
    padding: 0;
    width: 1200px;
    height: 1000px;
    overflow: hidden;
  }
  .stage {
    position: relative;
    width: 1200px;
    height: 1000px;
    background:
      radial-gradient(ellipse 900px 700px at 1200px 1000px, #ffffff 0%, rgba(255,255,255,0) 70%),
      linear-gradient(120deg, #000000 0%, #3a3a3a 25%, #8a8a8a 50%, #c8c8c8 75%, #f4f4f4 100%);
    font-family: "Merriweather", Georgia, serif;
  }
  .card {
    position: absolute;
    width: 588px;
    height: 286px;
    box-sizing: border-box;
    border: 8px solid var(--frame-red);
    box-shadow:
      inset 0 0 0 1px var(--frame-dark),
      inset 3px 3px 4px rgba(0,0,0,0.55),
      0 0 3px rgba(255,80,60,0.8);
  }
  .card--dark { left: 302px; top: 140px; background: var(--card-dark); color: var(--text-on-dark); }
  .card--light { left: 310px; top: 506px; background: var(--card-light); color: var(--text-on-light); }

  .brand {
    position: absolute;
    left: 11px;
    top: 11px;
    display: flex;
    align-items: center;
    gap: 10px;
  }
  .card--light .brand { left: 19px; top: 17px; }
  .brand__square {
    width: 58px;
    height: 58px;
    border-radius: 3px;
    background: var(--mark-red);
  }
  .brand__name {
    font-family: "Merriweather", Georgia, serif;
    font-weight: 700;
    font-size: 30px;
    color: var(--brand-grey);
    letter-spacing: 0.5px;
    white-space: nowrap;
  }
  .contact {
    position: absolute;
    left: 0;
    right: 0;
    top: 114px;
    text-align: center;
    font-size: 21px;
    line-height: 28px;
  }
  .contact p { margin: 0; }
</style>
</head>
<body>
  <main class="stage">
    <section class="card card--dark">
      <div class="brand">
        <div class="brand__square"></div>
        <span class="brand__name">Halvorsen Works</span>
      </div>
      <div class="contact">
        <p>(Name)</p>
        <p>(Phone)</p>
        <p>(Email)</p>
      </div>
    </section>

    <section class="card card--light">
      <div class="brand">
        <div class="brand__square"></div>
        <span class="brand__name">Halvorsen Works</span>
      </div>
      <div class="contact">
        <p>(Name)</p>
        <p>(Phone)</p>
        <p>(Email)</p>
      </div>
    </section>
  </main>
</body>
</html>
```